Dental Office business/appointment cards
Bramble Cove Dental Clinic, Cosmetic, Implant and Family Dentistry
Creative Brief
Simple
Tom Hasselback BSc, DDS
Dr.
2817 Pelham Avenue Niagara Falls, Ontario L3K 4T9
bcdentalcare@quillpost.net
www.bramblecovedentalcare.net
I need an appointment card on the back with time and date spaces and the text "48 business hours notice required for cancellations"

```html
<!DOCTYPE html>
<html lang="en">
<head>
<meta charset="utf-8">
<title>Bramble Cove Dental Clinic – Stationery</title>
<link href="https://fonts.googleapis.com/css2?family=Open+Sans:wght@400;600;700&display=swap" rel="stylesheet">
<style>
  :root{
    --bg:#e9e9e9;
    --paper:#ffffff;
    --blue:#2aa6df;
    --blue-light:#7fd0f2;
    --grey:#8a8d90;
    --grey-light:#c9cbcd;
    --grey-dark:#5e6266;
    --ink:#4a4d50;
    --shadow:0 2px 6px rgba(0,0,0,.25);
  }
  *{margin:0;padding:0;box-sizing:border-box}
  html,body{width:1200px;height:466px;overflow:hidden}
  body{background:var(--bg);font-family:"Open Sans",Arial,sans-serif;color:var(--ink);position:relative}
  .sheet{position:absolute;background:var(--paper);box-shadow:var(--shadow);overflow:hidden}
  .wave{position:absolute;left:0;bottom:0;width:100%;display:block}
  .brand{font-weight:700;color:var(--blue);white-space:nowrap;display:flex;align-items:center;gap:4px}
  .brand .dot{display:inline-block;border-radius:50%;background:var(--blue)}
  .small{font-size:5px;line-height:1.45;color:var(--grey-dark)}

  /* business cards */
  .card{width:96px;height:56px}
  .card-front{left:12px;top:88px}
  .card-back{left:12px;top:198px}
  .card .brand{position:absolute;left:6px;top:8px;font-size:6px}
  .card .brand .dot{width:6px;height:6px}
  .card-front .details{position:absolute;left:6px;top:20px;font-size:3.6px;line-height:1.4;color:var(--grey-dark)}
  .card-back .appt{position:absolute;left:6px;top:6px;right:6px;font-size:3.6px;line-height:1.5;color:var(--grey-dark)}
  .appt .field{display:flex;gap:2px;margin-top:2px}
  .appt .field span{flex:1;border-bottom:0.5px solid var(--grey)}
  .appt .notice{margin-top:4px;color:var(--blue);font-weight:600}

  /* letterheads */
  .letterhead{top:36px;width:266px;height:391px}
  .letterhead-one{left:257px}
  .letterhead-two{left:548px}
  .letterhead .brand{position:absolute;left:0;right:0;top:16px;justify-content:center;font-size:10px}
  .letterhead .brand .dot{width:9px;height:9px}
  .letterhead .contact{position:absolute;right:18px;top:14px;text-align:right;font-size:3.8px;line-height:1.5;color:var(--grey-dark)}
  .letterhead-one .brand{justify-content:flex-start;left:18px}
  .watermark{position:absolute;left:83px;top:80px;width:100px;height:100px;border-radius:50%;background:var(--blue-light);opacity:.18}

  /* envelopes */
  .envelope{left:869px;width:307px}
  .env-open{top:34px;height:146px;background:var(--blue)}
  .env-open .inner{position:absolute;left:0;right:0;bottom:0;height:84px;background:var(--paper)}
  .env-grey{top:154px;height:98px;background:var(--paper)}
  .env-white{top:259px;height:78px}
  .env-front{top:360px;height:82px}
  .envelope .flap{position:absolute;left:0;top:0;width:100%;display:block}
  .env-grey .brand,.env-white .brand{position:absolute;left:0;right:0;justify-content:center;font-size:7px}
  .env-grey .brand{top:56px}
  .env-white .brand{top:44px}
  .envelope .brand .dot{width:6px;height:6px}
  .env-front .brand{position:absolute;left:12px;top:10px;font-size:7px}
  .env-front .return{position:absolute;left:12px;top:22px;font-size:3.8px;line-height:1.5;color:var(--grey-dark)}
</style>
</head>
<body>

<!-- business card front -->
<div class="sheet card card-front">
  <div class="brand"><i class="dot"></i>Bramble Cove Dental Clinic</div>
  <div class="details">
    <strong>Dr. Tom Hasselback</strong> BSc, DDS<br>
    Cosmetic, Implant and Family Dentistry<br>
    2817 Pelham Avenue Niagara Falls, Ontario L3K 4T9<br>
    bcdentalcare@quillpost.net<br>
    www.bramblecovedentalcare.net
  </div>
  <svg class="wave" viewBox="0 0 96 14" preserveAspectRatio="none" height="14">
    <path d="M0 8 Q40 0 96 6 L96 14 L0 14Z" fill="var(--grey-light)"/>
    <path d="M0 11 Q45 4 96 9 L96 14 L0 14Z" fill="var(--blue)"/>
  </svg>
</div>

<!-- business card back: appointment -->
<div class="sheet card card-back">
  <div class="appt">
    <strong>Your next appointment</strong>
    <div class="field">Date <span></span></div>
    <div class="field">Time <span></span></div>
    <div class="notice">48 business hours notice required for cancellations</div>
  </div>
  <svg class="wave" viewBox="0 0 96 10" preserveAspectRatio="none" height="10">
    <path d="M0 5 Q40 0 96 4 L96 10 L0 10Z" fill="var(--grey-light)"/>
    <path d="M0 8 Q45 3 96 7 L96 10 L0 10Z" fill="var(--blue)"/>
  </svg>
</div>

<!-- letterhead option one -->
<div class="sheet letterhead letterhead-one">
  <div class="brand"><i class="dot"></i>Bramble Cove Dental Clinic</div>
  <div class="contact">
    2817 Pelham Avenue<br>Niagara Falls, Ontario L3K 4T9<br>
    bcdentalcare@quillpost.net<br>www.bramblecovedentalcare.net
  </div>
  <svg class="wave" viewBox="0 0 266 40" preserveAspectRatio="none" height="40">
    <path d="M0 18 Q110 2 266 16 L266 40 L0 40Z" fill="var(--grey-light)"/>
    <path d="M0 26 Q120 10 266 24 L266 40 L0 40Z" fill="var(--grey)"/>
    <path d="M0 32 Q130 18 266 30 L266 40 L0 40Z" fill="var(--blue)"/>
  </svg>
</div>

<!-- letterhead option two -->
<div class="sheet letterhead letterhead-two">
  <div class="brand"><i class="dot"></i>Bramble Cove Dental Clinic</div>
  <div class="watermark" role="img" aria-label="Faint clinic emblem area"></div>
  <svg class="wave" viewBox="0 0 266 40" preserveAspectRatio="none" height="40">
    <path d="M0 18 Q110 2 266 16 L266 40 L0 40Z" fill="var(--grey-light)"/>
    <path d="M0 26 Q120 10 266 24 L266 40 L0 40Z" fill="var(--grey)"/>
    <path d="M0 32 Q130 18 266 30 L266 40 L0 40Z" fill="var(--blue)"/>
  </svg>
</div>

<!-- envelope, open flap -->
<div class="sheet envelope env-open">
  <div class="inner"></div>
  <svg class="flap" viewBox="0 0 307 70" preserveAspectRatio="none" height="70">
    <path d="M0 0 H307 V20 Q250 60 153 64 Q56 60 0 20Z" fill="var(--blue)"/>
  </svg>
</div>

<!-- envelope, grey flap -->
<div class="sheet envelope env-grey">
  <svg class="flap" viewBox="0 0 307 46" preserveAspectRatio="none" height="46">
    <path d="M0 0 H307 V10 Q250 40 153 44 Q56 40 0 10Z" fill="var(--grey)"/>
  </svg>
  <div class="brand"><i class="dot"></i>Bramble Cove Dental Clinic</div>
</div>

<!-- envelope, white flap -->
<div class="sheet envelope env-white">
  <svg class="flap" viewBox="0 0 307 38" preserveAspectRatio="none" height="38">
    <path d="M0 0 Q56 30 153 34 Q250 30 307 0" fill="none" stroke="var(--grey-light)" stroke-width="1"/>
  </svg>
  <div class="brand"><i class="dot"></i>Bramble Cove Dental Clinic</div>
</div>

<!-- envelope front -->
<div class="sheet envelope env-front">
  <div class="brand"><i class="dot"></i>Bramble Cove Dental Clinic</div>
  <div class="return">2817 Pelham Avenue<br>Niagara Falls, Ontario L3K 4T9</div>
  <svg class="wave" viewBox="0 0 307 16" preserveAspectRatio="none" height="16">
    <path d="M0 7 Q130 0 307 6 L307 16 L0 16Z" fill="var(--grey-light)"/>
    <path d="M0 11 Q140 4 307 10 L307 16 L0 16Z" fill="var(--blue)"/>
  </svg>
</div>

</body>
</html>
```